New Label Design Project for Tinkers hollow wines

I would like to purchase a customized version of a design you have previously submitted - https://www.artpitchhub.com.au/design/57302946

We need a label that that we can use for our new vintage shiraz, Merlot and Pinot Noir products. This Label will be just 1 label that will be front and back label.
Please see attached

Target Market(s)

young and old wine drinkers

Industry/Entity Type

Wine

Colors

Designer to choose colors to be used in the design.

Requirements
Must have
• logo but also is a bit funky
Nice to have
• mixture of Funky and Modern

```html
<!DOCTYPE html>
<html lang="en">
<head>
<meta charset="utf-8">
<title>Tinkers Hollow Wines – Label Set</title>
<link rel="stylesheet" href="https://fonts.googleapis.com/css2?family=Cormorant+Garamond:wght@500;600&family=Open+Sans:wght@400&display=swap">
<style>
  :root {
    --page: #ffffff;
    --label-black: #050505;
    --wine-red: #a11d21;
    --brand-red: #c8202a;
    --gold-dark: #9c7546;
    --gold-light: #f1d9b6;
    --gold-text: #d6b57e;
    --ink-light: #e9e9e9;
    --band-ink: #2a1c10;
    --art-grey: #3a3a3a;
  }
  html, body { margin: 0; padding: 0; width: 800px; height: 1200px; overflow: hidden; background: var(--page); }
  .label-set {
    position: absolute; left: 12px; top: 356px;
    width: 945px; height: 595px;
    transform: scale(0.82); transform-origin: 0 0;
    font-family: "Cormorant Garamond", serif;
  }
  .neck-strip {
    position: absolute; top: 0; width: 49px; height: 477px;
    background: var(--label-black); border-radius: 25px;
  }
  .neck-strip__name {
    position: absolute; left: 50%; width: 130px; margin-left: -65px;
    text-align: center; color: var(--gold-text); font-size: 14px; font-weight: 600;
    transform: rotate(90deg); white-space: nowrap;
  }
  .neck-strip__name--top { top: 80px; }
  .neck-strip__name--bottom { top: 380px; }
  .neck-strip__mark {
    position: absolute; left: 16px; top: 228px; width: 16px; height: 16px;
    border-radius: 50%; border: 1.5px solid var(--gold-text); box-sizing: border-box;
  }
  .front-label {
    position: absolute; top: 5px; width: 357px; height: 380px;
    background: var(--label-black); color: var(--ink-light); text-align: center;
  }
  .front-label__ribbon {
    position: absolute; left: 125px; top: 0; width: 108px; height: 180px;
    background: var(--wine-red);
    clip-path: polygon(0 0, 100% 0, 100% 86%, 50% 100%, 0 86%);
  }
  .brand-mark {
    position: absolute; left: 164px; top: 60px; width: 30px; height: 30px;
    border-radius: 50%; background: var(--gold-text);
  }
  .front-label__brand {
    position: absolute; left: 0; right: 0; top: 104px;
    color: #ffffff; font-size: 34px; font-weight: 600; line-height: 32px;
  }
  .front-label__wine {
    position: absolute; left: 0; right: 0; top: 190px;
    font-size: 16px; letter-spacing: 2px; line-height: 20px;
  }
  .front-label__wine small { font-size: 12px; font-variant: small-caps; letter-spacing: 2px; }
  .front-label__art {
    position: absolute; left: 90px; top: 248px; width: 178px; height: 56px;
    background: linear-gradient(180deg, #1c1c1c, var(--art-grey));
    border-radius: 20px 20px 0 0;
  }
  .origin-band {
    position: absolute; left: 0; right: 0; top: 304px; height: 24px;
    background: linear-gradient(90deg, var(--gold-dark), var(--gold-light) 45%, var(--gold-light) 60%, var(--gold-dark));
    color: var(--band-ink); font-size: 18px; font-weight: 600; letter-spacing: 2px; line-height: 25px;
  }
  .front-label__volume {
    position: absolute; left: 0; right: 0; top: 352px;
    font-family: "Open Sans", sans-serif; font-size: 10px;
  }
  .back-label {
    position: absolute; top: 395px; width: 241px; height: 198px;
    background: var(--label-black); color: var(--ink-light); text-align: center;
  }
  .back-label .brand-mark { left: 112px; top: 12px; width: 18px; height: 18px; }
  .back-label__brand {
    position: absolute; left: 0; right: 0; top: 34px;
    color: var(--brand-red); font-size: 21px; font-weight: 600;
  }
  .back-label__wine {
    position: absolute; left: 0; right: 0; top: 72px;
    font-size: 11px; font-variant: small-caps; letter-spacing: 1px; line-height: 13px;
  }
  .back-label__notes {
    position: absolute; left: 8px; right: 8px; top: 101px;
    font-family: "Open Sans", sans-serif; font-size: 7.5px; line-height: 12px;
  }
  .back-label__origin {
    position: absolute; left: 12px; top: 129px;
    font-size: 10px; letter-spacing: 1px; text-align: left;
  }
  .back-label__legal {
    position: absolute; left: 12px; top: 146px; width: 130px; text-align: left;
    font-family: "Open Sans", sans-serif; font-size: 5px; line-height: 9.5px;
  }
  .back-label__code-space {
    position: absolute; left: 145px; top: 128px; width: 86px; height: 64px; background: #ffffff;
  }
</style>
</head>
<body>
<main class="label-set">

  <!-- Shiraz set -->
  <div class="neck-strip" style="left:0">
    <span class="neck-strip__name neck-strip__name--top">Tinkers Hollow</span>
    <span class="neck-strip__mark"></span>
    <span class="neck-strip__name neck-strip__name--bottom">Tinkers Hollow</span>
  </div>

  <section class="front-label" style="left:67px">
    <div class="front-label__ribbon"></div>
    <span class="brand-mark"></span>
    <div class="front-label__brand">Tinkers<br>Hollow</div>
    <div class="front-label__wine">2007 SHIRAZ<br><small>Mt. Benson</small></div>
    <div class="front-label__art" role="img" aria-label="Stacked wine barrels illustration"></div>
    <div class="origin-band">WINE OF AUSTRALIA</div>
    <div class="front-label__volume">750mL</div>
  </section>

  <section class="back-label" style="left:124px">
    <span class="brand-mark"></span>
    <div class="back-label__brand">Tinkers Hollow</div>
    <div class="back-label__wine">2007 Shiraz Mt. Benson<br>South Australia</div>
    <p class="back-label__notes" style="margin:0">This mature, smooth Shiraz matches most savoury foods<br>and any occasion. Drink now and enjoy.</p>
    <div class="back-label__origin">WINE OF AUSTRALIA</div>
    <div class="back-label__legal">HOLLOWFIELD ESTATES PTY LTD<br>Kingsford Victoria 3999 Australia<br>13.6% ALC/VOL<br>APPROX. 8.0 STANDARD DRINKS<br>Preservative 220 added.</div>
    <div class="back-label__code-space"></div>
  </section>

  <!-- Pinot Noir set -->
  <section class="front-label" style="left:502px">
    <div class="front-label__ribbon"></div>
    <span class="brand-mark"></span>
    <div class="front-label__brand">Tinkers<br>Hollow</div>
    <div class="front-label__wine"><small>Pinot Noir</small><br>2019</div>
    <div class="front-label__art" role="img" aria-label="Horse-drawn carriage illustration"></div>
    <div class="origin-band">WINE OF AUSTRALIA</div>
    <div class="front-label__volume">750mL</div>
  </section>

  <section class="back-label" style="left:558px">
    <span class="brand-mark"></span>
    <div class="back-label__brand">Tinkers Hollow</div>
    <div class="back-label__wine">2019 Pinot Noir<br>South Australia</div>
    <p class="back-label__notes" style="margin:0">This mature, smooth Shiraz matches most savoury foods<br>and any occasion. Drink now and enjoy.</p>
    <div class="back-label__origin">WINE OF AUSTRALIA</div>
    <div class="back-label__legal">HOLLOWFIELD ESTATES PTY LTD<br>Kingsford Victoria 3999 Australia<br>13.6% ALC/VOL<br>APPROX. 8.0 STANDARD DRINKS<br>Preservative 220 added.</div>
    <div class="back-label__code-space"></div>
  </section>

  <div class="neck-strip" style="left:897px">
    <span class="neck-strip__name neck-strip__name--top">Tinkers Hollow</span>
    <span class="neck-strip__mark"></span>
    <span class="neck-strip__name neck-strip__name--bottom">Tinkers Hollow</span>
  </div>

</main>
</body>
</html>
```